Venture Capital Firm Needs Website Redesign

We need a bold revamp of our website (https://halvermoor.vc/)
which at the moment looks washed out. We want a crisp, fresh and unique look. Feel free to keep as much or as little content in the site. The only thing we need to keep is a team section. The site should convey a clear distinction between our 3 product lines: Venture Capital, Private Credit, and Crypto. Two versions of our logo are attached and they should not change. For design inspirations, we like http://www.pelmdrift.com/ for a more simple site and for a more built out site we like http://tallowbeck.com/

Updates
Industry/Entity Type
Investment
Coding
Coded - Design and coding required
Number of Pages Required
1 page
Font styles to use
Colors
Designer to choose colors to be used in the design.
Requirements
Must have
- - Clear distinction between our 3 product lines: Venture Capital, Private Credit
- - Team section

Nice to have
- Some really creative aspect like http://www.pelmdrift.com/ has with the distinction between first, second, and third kind

```html
<!DOCTYPE html>
<html lang="en">
<head>
<meta charset="utf-8">
<title>Halvermoor</title>
<link rel="stylesheet" href="https://fonts.googleapis.com/css2?family=Jost:wght@400;500;700&family=Noto+Sans:wght@400&display=swap">
<style>
  :root {
    --ink: #2f2f2f;
    --frame: #3a3a3a;
    --green: #92a640;
    --green-text: #8a9c38;
    --bg-light: #f3f3f3;
    --bg-mid: #e7e7e7;
    --tile: #e9e9e9;
    --white: #ffffff;
  }
  * { margin: 0; padding: 0; box-sizing: border-box; }
  html, body { width: 1200px; height: 1194px; overflow: hidden; }
  body {
    position: relative;
    background: linear-gradient(160deg, var(--bg-light) 0%, var(--bg-mid) 100%);
    font-family: "Noto Sans", sans-serif;
    color: var(--ink);
  }
  .site-header {
    position: absolute; left: 80px; top: 40px; width: 1040px; height: 40px;
  }
  .brand {
    position: absolute; left: 0; top: 0;
    font-family: "Jost", sans-serif; font-weight: 400; font-size: 27px;
    letter-spacing: -0.5px; color: var(--ink);
  }
  .main-nav {
    position: absolute; right: 69px; top: 11px; display: flex; gap: 33px;
    font-family: "Jost", sans-serif; font-size: 12.5px; text-transform: uppercase;
  }
  .main-nav a { color: var(--ink); text-decoration: none; }
  .menu-toggle { position: absolute; right: 0; top: 5px; width: 31px; height: 28px; }
  .hero-title {
    position: absolute; right: 112px; top: 132px; text-align: right;
    font-family: "Jost", sans-serif; font-weight: 700; font-size: 58px;
    line-height: 56px; letter-spacing: -1px; text-transform: uppercase; color: var(--ink);
  }
  .accent { color: var(--green-text); }
  .hero-art {
    position: absolute; left: 100px; top: 250px; width: 680px; height: 350px;
    background: radial-gradient(ellipse at 45% 55%, #dcdcdc 0%, rgba(230,230,230,0) 70%);
  }
  .portfolio {
    position: absolute; left: 81px; top: 600px; width: 371px;
    display: grid; grid-template-columns: 182px 182px; grid-auto-rows: 158px; gap: 8px;
  }
  .portfolio-tile {
    border: 8px solid var(--frame); background: var(--tile);
    display: flex; align-items: center; justify-content: center;
    font-family: "Noto Sans", sans-serif; font-size: 15px; color: #2c4a5a; text-align: center;
  }
  .venture {
    position: absolute; left: 497px; top: 642px; width: 570px;
  }
  .section-kicker {
    font-family: "Jost", sans-serif; font-size: 32px; line-height: 32px;
    color: var(--green-text); text-transform: uppercase;
  }
  .section-title {
    font-family: "Jost", sans-serif; font-size: 52px; line-height: 46px;
    color: var(--ink); text-transform: uppercase; letter-spacing: -1px;
  }
  .venture p { margin-top: 18px; font-size: 18.5px; line-height: 26.5px; }
  .about-band {
    position: absolute; left: 0; top: 988px; width: 1200px; height: 206px;
    background: var(--green);
  }
  .band-notch { position: absolute; left: 532px; top: 0; }
  .about-heading {
    position: absolute; left: 80px; top: 74px;
    font-family: "Jost", sans-serif; text-transform: uppercase;
  }
  .about-heading .kicker { display: block; font-size: 32px; line-height: 30px; color: var(--white); }
  .about-heading .title { display: block; font-size: 46px; line-height: 44px; color: var(--ink); }
  .about-band p {
    position: absolute; left: 221px; top: 78px; width: 570px;
    font-size: 19px; line-height: 26.5px; color: var(--white);
  }
  .about-art {
    position: absolute; left: 830px; top: 66px; width: 240px; height: 240px; border-radius: 50%;
    background: radial-gradient(circle at 50% 50%, #dff08a 0%, #c0d63c 45%, rgba(146,166,64,0) 72%);
  }
</style>
</head>
<body>
  <header class="site-header">
    <div class="brand">HALVERMOOR</div>
    <nav class="main-nav">
      <a href="#">Venture</a>
      <a href="#">Private Credit</a>
      <a href="#">Crypto</a>
      <a href="#">About Us</a>
      <a href="#">Our Team</a>
      <a href="#">Blog</a>
    </nav>
    <svg class="menu-toggle" viewBox="0 0 31 28" aria-label="Menu">
      <rect x="0" y="0" width="31" height="3" fill="#2f2f2f"/>
      <rect x="0" y="12" width="31" height="3" fill="#2f2f2f"/>
      <rect x="0" y="24" width="31" height="3" fill="#2f2f2f"/>
    </svg>
  </header>

  <h1 class="hero-title">
    Halvermoor<br>operates at the<br>intersection of<br>technology <span class="accent">and</span><br>novel asset<br>classes
  </h1>

  <div class="hero-art" role="img" aria-label="A green paper boat with a flag leading a line of white paper boats"></div>

  <div class="portfolio">
    <div class="portfolio-tile">Corvane Capital Group</div>
    <div class="portfolio-tile">lumacode</div>
    <div class="portfolio-tile" style="font-size:26px">pipwalk</div>
    <div class="portfolio-tile" style="font-size:22px">Ledgerloop</div>
  </div>

  <section class="venture">
    <div class="section-kicker">Venture</div>
    <h2 class="section-title">Capital</h2>
    <p>We invest in early-stage startups led by founders who are passionate and knowledgeable about the markets they serve. We have our own software developers and product managers.<br>We work with the founders in our portfolio to help them bring products to market, earning equity for this work and for the cash we invest in their companies.</p>
  </section>

  <section class="about-band">
    <svg class="band-notch" width="86" height="48" viewBox="0 0 86 48">
      <polygon points="0,0 86,0 43,48" fill="#e9e9e9"/>
    </svg>
    <h2 class="about-heading"><span class="kicker">About</span><span class="title">Us</span></h2>
    <p>Halvermoor operates three businesses that bridge technology and finance. We invest in pre-seed venture capital, and build software for the companies we invest in. We manage direct private credit funds that provide private credit capital to alternative private credit platforms, enabling them to finance the loans they origi-nate.</p>
    <div class="about-art" role="img" aria-label="Bright lime splash illustration with glowing rings"></div>
  </section>
</body>
</html>
```